Letterhead and Business card for Construction company

We need a letterhead and business card with our new company logo. We are based in NY. We develop and build properties.

The design should incorporate some unique feature from the logo (shape, font...). it should look like an extension from it.

Design should be clean and elegant, professional, not too busy.

The letterhead should include:
Logo (attached)
Address
Phone
Email

Please find the attached logo images and AI file.

Target Market(s)

Construction industry professionals

Industry/Entity Type

Construction, Development

Font styles to use
Sans Serif

Colors

Designer to choose colors to be used in the design.

Requirements
Must have
• Design should incorporate logo elements, additional assets are welcome. I'd like to see some other shapes / images invorporated too.

```html
<!DOCTYPE html>
<html lang="en">
<head>
<meta charset="utf-8">
<title>Halden Build — Letterhead</title>
<link href="https://fonts.googleapis.com/css2?family=Saira:wght@400;700&display=swap" rel="stylesheet">
<style>
  :root {
    --orange: #ee7b1f;
    --charcoal: #2b2a28;
    --paper: #ffffff;
    --ink: #2b2a28;
  }
  html, body {
    margin: 0;
    padding: 0;
    overflow: hidden;
    background: var(--paper);
  }
  .letterhead {
    position: relative;
    width: 899px;
    height: 1200px;
    background: var(--paper);
    font-family: "Saira", Arial, sans-serif;
    color: var(--ink);
    overflow: hidden;
  }
  .band {
    position: absolute;
    height: 40px;
  }
  .band--top-orange { top: 0; left: 0; width: 601px; background: var(--orange); }
  .band--top-dark { top: 0; left: 616px; width: 283px; background: var(--charcoal); }
  .band--bottom-dark { bottom: 0; left: 0; width: 282px; background: var(--charcoal); }
  .band--bottom-orange { bottom: 0; left: 298px; width: 601px; background: var(--orange); }

  .brand {
    position: absolute;
    top: 108px;
    left: 42px;
    display: flex;
    align-items: center;
    gap: 8px;
  }
  .brand__mark {
    width: 14px;
    height: 14px;
    background: var(--orange);
  }
  .brand__name {
    font-weight: 700;
    font-size: 22px;
    letter-spacing: 1px;
    color: var(--charcoal);
    text-transform: uppercase;
    line-height: 1;
  }

  .contact {
    position: absolute;
    left: 42px;
    top: 1089px;
    margin: 0;
    padding: 0;
    list-style: none;
  }
  .contact__item {
    display: flex;
    align-items: center;
    height: 21px;
    font-size: 13px;
    letter-spacing: 0.3px;
  }
  .contact__icon {
    width: 12px;
    height: 12px;
    margin-right: 13px;
    flex: none;
  }
</style>
</head>
<body>
<div class="letterhead">
  <div class="band band--top-orange"></div>
  <div class="band band--top-dark"></div>

  <div class="brand">
    <span class="brand__mark"></span>
    <span class="brand__name">Halden Build</span>
  </div>

  <ul class="contact">
    <li class="contact__item">
      <svg class="contact__icon" viewBox="0 0 12 12" aria-hidden="true">
        <rect width="12" height="12" rx="2.5" fill="var(--orange)"/>
        <path d="M4 3.2 L5.2 4.6 L4.6 5.3 Q5.4 6.8 6.8 7.5 L7.5 6.9 L8.8 8.1 L8 9 Q5 8.6 3.2 4 Z" fill="#fff"/>
      </svg>
      (000) 234 5678
    </li>
    <li class="contact__item">
      <svg class="contact__icon" viewBox="0 0 12 12" aria-hidden="true">
        <rect width="12" height="12" rx="2.5" fill="var(--orange)"/>
        <rect x="2.8" y="3.8" width="6.4" height="4.4" fill="none" stroke="#fff" stroke-width="0.9"/>
        <path d="M2.8 3.8 L6 6.4 L9.2 3.8" fill="none" stroke="#fff" stroke-width="0.9"/>
      </svg>
      hello@haldenbuild.com
    </li>
    <li class="contact__item">
      <svg class="contact__icon" viewBox="0 0 12 12" aria-hidden="true">
        <rect width="12" height="12" rx="2.5" fill="var(--orange)"/>
        <path d="M6 9.4 Q3.2 6.4 3.2 5 A2.8 2.8 0 0 1 8.8 5 Q8.8 6.4 6 9.4 Z" fill="none" stroke="#fff" stroke-width="0.9"/>
        <circle cx="6" cy="5" r="1" fill="#fff"/>
      </svg>
      Name, Street no., area, city pincode
    </li>
  </ul>

  <div class="band band--bottom-dark"></div>
  <div class="band band--bottom-orange"></div>
</div>
</body>
</html>
```